Bourbon label design for bourbon brand. Looking to freshen our current label.

I need a Bourbon label design for our rebranded Bourbon bottle. Label should include picture of our horse and our logo on the bottle. Front Label is 3.5 inches wide and 6 inches tall, back label is 4 inches tall and 3 inches wide. Back label can be a simple plain logo like the one in the brief. I have included a design of our current bottle and label. We want to stay close to the current color schemes but want a fresh rebrand of the design. The label needs to be the correct size on a tall bottle like pictured.

Target Market(s)

Our Bourbon members, 30-50 year old males

Requirements
Must have
• Picture of our horse, our B logo , straight Bourbon whiskey on the front. Room to edit text on the back label.

```html
<!DOCTYPE html>
<html lang="en">
<head>
<meta charset="utf-8">
<title>Darkstride Straight Bourbon Whiskey – Label Set</title>
<link href="https://fonts.googleapis.com/css2?family=Oswald:wght@500;600;700&family=Nunito+Sans:wght@400&display=swap" rel="stylesheet">
<style>
  :root {
    --board: #dcdcdc;
    --label-black: #000000;
    --ink-white: #ffffff;
    --ink-grey: #8a8a8a;
    --mark-grey: #58585a;
    --strip-white: #ffffff;
    --photo-light: #c4c4c4;
    --photo-dark: #5e5e5e;
  }
  * { box-sizing: border-box; margin: 0; padding: 0; }
  html, body { width: 1000px; height: 1200px; overflow: hidden; }
  body {
    background: var(--board);
    position: relative;
    font-family: "Oswald", sans-serif;
    color: var(--ink-white);
  }

  /* Front label */
  .front-label {
    position: absolute;
    left: 82px; top: 80px;
    width: 329px; height: 564px;
    background: var(--strip-white);
  }
  .front-label__panel {
    position: absolute; inset: 0 0 27px 0;
    background: var(--label-black);
    text-align: center;
  }
  .brand-name {
    position: absolute; left: 0; right: 0;
    font-weight: 700; letter-spacing: 0.5px; text-transform: uppercase;
    color: var(--ink-white);
  }
  .front-label .brand-name { top: 44px; font-size: 44px; line-height: 56px; }
  .product-type {
    position: absolute; left: 0; right: 0;
    font-weight: 600; text-transform: uppercase; letter-spacing: 0.4px;
  }
  .front-label .product-type { top: 105px; font-size: 17px; line-height: 22px; }
  .established {
    position: absolute; left: 141px; width: 47px; top: 145px;
    border-top: 1px solid var(--ink-white);
    border-bottom: 1px solid var(--ink-white);
    padding: 4px 0 5px;
    font-size: 11px; line-height: 14px; font-weight: 600; letter-spacing: 0.3px;
  }
  .horse-photo {
    position: absolute; left: 121px; top: 193px;
    width: 117px; height: 236px;
    border-radius: 40px 40px 30px 30px;
    background: radial-gradient(ellipse at 50% 35%, var(--photo-light), var(--photo-dark));
  }
  .finish-notes {
    position: absolute; left: 0; right: 0; top: 449px;
    font-size: 12px; font-weight: 600; line-height: 19px; text-transform: uppercase;
  }
  .bottle-details {
    position: absolute; left: 24px; right: 24px; top: 519px;
    display: flex; justify-content: space-between;
    font-size: 10px; line-height: 14px; font-weight: 600; color: var(--ink-grey); text-transform: uppercase;
  }

  /* Back label */
  .back-label {
    position: absolute;
    left: 107px; top: 747px;
    width: 286px; height: 377px;
    background: var(--label-black);
    text-align: center;
  }
  .back-label__mark {
    position: absolute; left: 0; right: 0; top: 58px;
    font-size: 26px; line-height: 34px; font-weight: 700; color: var(--mark-grey);
    text-transform: uppercase; letter-spacing: 0.5px;
  }
  .back-label .brand-name { top: 137px; font-size: 26px; line-height: 34px; }
  .back-label .product-type { top: 171px; font-size: 9.5px; line-height: 12px; }
  .back-copy {
    position: absolute; left: 31px; right: 31px; top: 200px;
    font-family: "Nunito Sans", sans-serif;
    font-size: 11px; line-height: 13.2px;
  }
</style>
</head>
<body>
  <section class="front-label" aria-label="Front label">
    <div class="front-label__panel">
      <h1 class="brand-name">Darkstride</h1>
      <p class="product-type">Straight Bourbon Whiskey</p>
      <p class="established">EST. 2016</p>
      <div class="horse-photo" role="img" aria-label="Black and white photograph of the brand's racehorse with jockey galloping toward the viewer"></div>
      <p class="finish-notes">Single Barrel<br>Barrel Strength</p>
      <div class="bottle-details">
        <span>Barrel No.</span>
        <span>Aged/Years</span>
        <span>Alc./Vol.</span>
      </div>
    </div>
  </section>

  <section class="back-label" aria-label="Back label">
    <p class="back-label__mark">Darkstride</p>
    <h2 class="brand-name">Darkstride</h2>
    <p class="product-type">Straight Bourbon Whiskey</p>
    <p class="back-copy">Lorem ipsum dolor sit amet, consectetur adipiscing elit. Quisque placerat sem at nunc venenatis venenatis. Vestibulum dapibus dui lectus, non accumsan mauris tincidunt et. In non viverra turpis. Aenean id finibus magna, et feugiat ipsum. Proin laoreet gravida lorem nec porta. Suspendisse a neque dictum, tempus lorem ac, suscipit dolor. Fusce id eleifend dolor. Quisque rhoncus sem vel tortor dapibus accumsan.</p>
  </section>
</body>
</html>
```